Vereins Website
Zielgruppe
Webiste für den Verein 'Katzenhain Oberlau' (details siehe Anhang).
Ziel der Website:
- Sponsoren finden
- Vereinsmitglieder finden & Interessen bündeln.
Aufgabenstellung
Die Webiste sollt aufgeräumt, übersichtlich und freundlich wirken.

```html
<!DOCTYPE html>
<html lang="de">
<head>
<meta charset="utf-8">
<title>Verein Katzenhain Oberlau</title>
<link href="https://fonts.googleapis.com/css2?family=Arimo:wght@400;700&display=swap" rel="stylesheet">
<style>
:root{
  --orange:#f18f00;
  --ink:#222222;
  --white:#ffffff;
  --field:#e2e2e2;
  --tile:#dadada;
  --tile-dark:#bdbdbd;
  --grey-band:#e6e6e6;
  --footer:#7b7b7b;
  --peach:#f8c796;
}
*{margin:0;padding:0;box-sizing:border-box}
html,body{width:1200px;height:3266px;overflow:hidden}
body{position:relative;background:var(--white);font-family:"Arimo",Arial,sans-serif;color:var(--ink)}
.abs{position:absolute}
.center{left:0;width:1200px;text-align:center}
.site-header{top:0;left:0;width:1200px;height:160px;background:var(--orange)}
.header-kicker{top:66px;font-size:18px;letter-spacing:7px;color:var(--ink)}
.header-name{top:92px;font-size:44px;font-weight:700;color:var(--white);letter-spacing:1px;text-transform:uppercase}
.hero{top:160px;left:0;width:1200px;height:619px;background:linear-gradient(180deg,#6f7466 0%,#7d6a4f 35%,#a07a4e 65%,#8c7356 100%)}
.hero-title{top:574px;font-size:33px;font-weight:700;line-height:40px;letter-spacing:1.5px;color:var(--white);text-shadow:0 2px 4px rgba(0,0,0,.5)}
.btn{display:flex;align-items:center;justify-content:center;font-size:9px;font-weight:700;letter-spacing:2.5px;text-transform:uppercase;box-shadow:0 2px 3px rgba(0,0,0,.25)}
.btn-orange{background:var(--orange);color:var(--white)}
.btn-white{background:var(--white);color:var(--ink)}
.btn-light{font-weight:400;letter-spacing:3px}
.intro-title{top:850px;font-size:33px;font-weight:700;line-height:39px;letter-spacing:1.5px;color:var(--orange)}
.intro-text{top:947px;font-size:11.5px;line-height:18.8px;letter-spacing:3px;color:var(--ink)}
.form-title{top:1150px;font-size:21px;font-weight:700;letter-spacing:1px}
.label{font-size:12px;letter-spacing:3px}
.field{background:var(--field)}
.form-note{top:1526px;font-size:12px;line-height:17px;letter-spacing:.5px}
.help-title{top:1690px;font-size:42px;font-weight:700;letter-spacing:2px;color:var(--orange)}
.help-sub{top:1738px;font-size:27px;letter-spacing:5px}
.pet-image{top:1805px;left:340px;width:510px;height:201px;background:linear-gradient(180deg,#5b3a22 0%,#c3742f 55%,#2a1d16 100%);border-radius:200px 200px 0 0}
.donate-band{top:2006px;left:0;width:1200px;height:218px;background:var(--orange);color:var(--white)}
.donate-band h2{position:absolute;top:38px;width:100%;text-align:center;font-size:31px;letter-spacing:1.5px}
.donate-line{position:absolute;width:100%;text-align:center;font-size:19px;letter-spacing:1px}
.section-title{font-size:29px;font-weight:700;letter-spacing:2px}
.tile{background:var(--tile)}
.tile-feature{background:var(--tile-dark);color:var(--white);display:flex;align-items:center;justify-content:center;text-align:center;font-size:18px;line-height:23px;letter-spacing:1px}
.small-bold{top:2690px;font-size:11px;font-weight:700}
.small-line{top:2707px;font-size:10.5px;letter-spacing:.3px;color:#444}
.pay{display:flex;align-items:center;justify-content:center;gap:7px;font-size:18px;font-weight:700;color:var(--ink)}
.pay-mark{width:11px;height:11px;background:var(--orange)}
.pay-slip{background:var(--peach);font-size:8.5px;font-weight:400}
.contact-band{top:2870px;left:0;width:1200px;height:336px;background:var(--grey-band)}
.contact-title{top:2915px;font-size:19px;font-weight:700;letter-spacing:1.5px}
.input-white{background:var(--white);padding:13px 10px 0;font-size:13px;letter-spacing:3px}
.site-footer{top:3206px;left:0;width:1200px;height:60px;background:var(--footer);color:var(--white);font-size:13.5px;letter-spacing:.5px;display:flex;align-items:center;justify-content:center}
</style>
</head>
<body>

<header class="site-header abs">
  <div class="header-kicker abs center">VEREIN</div>
  <div class="header-name abs center">Katzenhain Oberlau</div>
</header>

<section class="hero abs" role="img" aria-label="Foto: Tier wälzt sich entspannt auf einer trockenen Wiese"></section>
<h1 class="hero-title abs center">WERDEN SIE VEREINSMITGLIED UND<br>UNTERSTÜTZEN UNSER PROJEKT</h1>
<div class="btn btn-orange abs" style="top:678px;left:408px;width:177px;height:32px">Mitglied werden</div>
<div class="btn btn-white abs" style="top:678px;left:625px;width:177px;height:32px">Sponsor werden</div>

<h2 class="intro-title abs center">EIN BEGEGNUNGSORT FÜR DIE GANZE REGION,<br>VON DEM ALLE PROFITIEREN.</h2>
<p class="intro-text abs center">NACH DEM VORBILD VON <b>OSTWIL</b> MÖCHTEN WIR IN OBERLAU EINEN<br>GESCHÜTZTEN KATZENGARTEN AUF DIE BEINE STELLEN UND DAMIT<br>DAS WOHLERGEHEN DER KATZEN FÖRDERN.<br>IM GESICHERTEN GARTEN KÖNNEN DIE KATZEN OHNE GEFAHR SPIELEN, SICH<br>AUSTOBEN UND SOZIALISIEREN.<br>GLEICHZEITIG SCHAFFT DIES EINEN RAUM, IN DEM SICH DIE KATZENHALTER TREFFEN UND<br>AUSTAUSCHEN KÖNNEN.</p>

<h3 class="form-title abs center">PROJEKT UNTERSTÜTZEN UND VEREINSMITGLIED* WERDEN:</h3>
<div class="label abs" style="top:1206px;left:304px">VORNAME</div>
<div class="label abs" style="top:1206px;left:623px">NACHNAME</div>
<div class="field abs" style="top:1229px;left:295px;width:301px;height:38px"></div>
<div class="field abs" style="top:1229px;left:614px;width:301px;height:38px"></div>
<div class="label abs" style="top:1285px;left:304px">STRASSE | HAUSNUMMER</div>
<div class="field abs" style="top:1308px;left:295px;width:620px;height:37px"></div>
<div class="label abs" style="top:1363px;left:304px">PLZ | ORT</div>
<div class="field abs" style="top:1386px;left:295px;width:620px;height:37px"></div>
<div class="label abs" style="top:1442px;left:304px">E-MAIL-ADRESSE</div>
<div class="field abs" style="top:1465px;left:295px;width:620px;height:37px"></div>
<p class="form-note abs center">* EINE VEREINSMITGLIEDSCHAFT IST DERZEIT NOCH KOSTENLOS.<br>SIE UNTERSTÜTZEN DEN VEREIN DAMIT IDEELL.</p>
<div class="btn btn-orange btn-light abs" style="top:1577px;left:498px;width:177px;height:32px">Absenden</div>

<h2 class="help-title abs center">HELFEN SIE UNS</h2>
<div class="help-sub abs center">DIESES PROJEKT ZU VERWIRKLICHEN</div>
<div class="pet-image abs" role="img" aria-label="Foto: Tier schaut neugierig über den Rand"></div>

<section class="donate-band abs">
  <h2>SPENDENKONTO<span style="font-weight:400;font-size:22px">:</span></h2>
  <div class="donate-line" style="top:84px">KATZENHAIN OBERLAU</div>
  <div class="donate-line" style="top:122px">IBAN: 98 00000 00000 00000 9</div>
  <div class="donate-line" style="top:160px">BIC: 6553873</div>
</section>

<h2 class="section-title abs center" style="top:2274px">FÜR SPONSOREN</h2>
<div class="tile abs" style="top:2338px;left:342px;width:122px;height:120px"></div>
<div class="tile abs" style="top:2338px;left:479px;width:122px;height:120px"></div>
<div class="tile-feature abs" style="top:2338px;left:616px;width:259px;height:120px">HIER KÖNNTE<br>IHR LOGO STEHEN</div>
<div class="tile abs" style="top:2472px;left:342px;width:260px;height:120px"></div>
<div class="tile abs" style="top:2472px;left:616px;width:121px;height:120px"></div>
<div class="tile abs" style="top:2472px;left:754px;width:121px;height:120px"></div>

<h2 class="section-title abs center" style="top:2646px">FÜR PRIVTE SPENDEN</h2>
<div class="small-bold abs center">SPENDENKONTO:</div>
<div class="small-line abs center">KATZENHAIN OBERLAU · IBAN: 98 00000 00000 00000 9 · BIC: 6553873</div>
<div class="pay abs" style="top:2758px;left:330px;width:90px;height:55px"><span class="pay-mark"></span>Zahlfix</div>
<div class="pay abs" style="top:2758px;left:430px;width:145px;height:55px"><span class="pay-mark"></span>Postkonto</div>
<div class="pay abs" style="top:2758px;left:595px;width:140px;height:55px"><span class="pay-mark"></span>Netzpay</div>
<div class="pay pay-slip abs" style="top:2768px;left:751px;width:128px;height:32px">EINZAHLUNGSSCHEIN</div>

<section class="contact-band abs"></section>
<h3 class="contact-title abs center">WIR FREUEN UNS AUF IHRE ANREGUNGEN &amp; IDEEN:</h3>
<div class="input-white abs" style="top:2960px;left:275px;width:324px;height:40px">NAME</div>
<div class="input-white abs" style="top:2960px;left:620px;width:324px;height:40px">E-MAIL-ADRESSE</div>
<div class="input-white abs" style="top:3019px;left:275px;width:669px;height:83px">IHRE NACHRICHT</div>
<div class="btn btn-orange btn-light abs" style="top:3121px;left:495px;width:192px;height:35px">Absenden</div>

<footer class="site-footer abs">COPYRIGHT © 2019 | INFO@KATZENHAIN-OBERLAU.CH</footer>

</body>
</html>
```